"Harlow's True Grain Woodwork" with a logo of a saw blade and handplane combined

Need a business card logo with a saw blade and hand plane
combined with Harlow's True Grain Woodwork on it, and a unique design.

Woodworking has been in my family for generations, from carpentry, to milling logs for old farm homes and barns in the 1930's and 1940's. My grandfather had a small carpentry business from his home,and passed his skills down to my father who also did woodworking from his own small business. Having the passion for woodwork in my blood, I'm trying to continue with my own small business doing custom fine woodwork such as tables, small cabinetry and even outdoor projects to suite the customers needs. All my projects start with a rough piece of lumber, what ever the species suited for the project, and is milled to dimensions , assembled, and finished all by hand for a true handcrafted project.

My target market would be people who want a custom handmade piece, something that they can't find in stores and is unique. Also people who are willing to pay and appreciate the value, which is sometimes a hard market to find.

As far as design, I think I would like to get a sleek looking saw blade on the card combined with a hand plane some how. Background colour maybe a dark wood texture or grey? Colours I like are grey, black, reds, white, yellows but depending on how the card is looking I'm not afraid to use a cool colour to make something stand out. Just want the card to flow ,look clean and unique. Lettering I like serif and script or something similar to these that looks good on the card.

Facebook page is under Harlow's True Grain Woodwork
Updates

If I could get logo on the card, a saw blade, hand plane or combine both together would be nice! Added Saturday, June 11, 2016

Target Market(s)

People that like a unique hand made project built to last

Industry/Entity Type

Business

Contact Information for Business Card

Harlows True Grain Woodwork
Hand crafted by: Owen Harlow
Phone: 905 718-2265
Address: 412 Birchmont Rd. Niagara-On-The-Lake Ont.
Email: harlowstruegrain@mailpost.example
Facebook: Harlows True Grain Woodwork
prefer icons for the info!

Font styles to use
Serif
Script

Requirements
Must have
• Nice clean look, little bit bold with an elegant taste
• Prefer black lettering
Nice to have
• I like silver for the saw blade and silver with brown handles on the hand plane!
Should not have
• Bright colours

```html
<!DOCTYPE html>
<html lang="en">
<head>
<meta charset="utf-8">
<title>Harlow's True Grain Woodwork – Business Card</title>
<link rel="stylesheet" href="https://fonts.googleapis.com/css2?family=Cardo:ital,wght@0,400;0,700;1,400&family=Oswald:wght@700&family=Open+Sans:ital,wght@0,600;1,600&display=swap">
<style>
  :root {
    --page-bg: #2a2a2a;
    --wood-top-light: #a99f91;
    --wood-top-dark: #8c8274;
    --wood-low-light: #c7c3bb;
    --wood-low-dark: #a8a39a;
    --ink: #121212;
    --band: #141414;
    --tagline: #b4a68c;
    --tool-dark: #1a1a1a;
    --tool-mid: #3b3733;
  }
  * { margin: 0; padding: 0; box-sizing: border-box; }
  html, body { width: 1200px; height: 1200px; overflow: hidden; }
  body { background: var(--page-bg); position: relative; }

  .business-card {
    position: absolute;
    left: 100px; top: 314px;
    width: 1000px; height: 572px;
    overflow: hidden;
    background: linear-gradient(180deg, var(--wood-top-light), var(--wood-top-dark));
  }

  .lower-planks {
    position: absolute;
    left: 0; right: 0; top: 266px; bottom: 0;
    background: linear-gradient(180deg, var(--wood-low-light), var(--wood-low-dark));
  }
  .plank-seam {
    position: absolute; left: 0; right: 0; height: 3px;
    background: rgba(60, 55, 48, 0.35);
  }

  .tool-mark {
    position: absolute;
    border-radius: 6px;
    background: linear-gradient(90deg, var(--tool-dark), var(--tool-mid));
  }
  .tool-mark--header { left: 52px; top: 50px; width: 130px; height: 76px; }
  .tool-mark--band {
    right: 36px; top: 226px; width: 130px; height: 40px;
    background: linear-gradient(90deg, #2e2a27, #4e4843);
  }

  .brand-name {
    position: absolute;
    left: 196px; top: 132px;
    font-family: "Cardo", serif;
    font-weight: 700;
    font-size: 50px;
    line-height: 1;
    color: var(--ink);
    white-space: nowrap;
  }

  .tagline-band {
    position: absolute;
    left: 0; right: 0; top: 226px; height: 40px;
    background: var(--band);
  }
  .tagline {
    position: absolute;
    right: 190px; top: 7px;
    font-family: "Open Sans", sans-serif;
    font-style: italic; font-weight: 600;
    font-size: 19px;
    color: var(--tagline);
    white-space: nowrap;
  }

  .owner-name {
    position: absolute;
    left: 56px; top: 272px;
    font-family: "Oswald", sans-serif;
    font-weight: 700; font-size: 34px;
    line-height: 48px;
    letter-spacing: 2px;
    color: var(--ink);
  }

  .contact-list {
    position: absolute;
    left: 56px; top: 326px;
    list-style: none;
  }
  .contact-item {
    display: flex; align-items: center; gap: 16px;
    height: 40px;
    font-family: "Open Sans", sans-serif;
    font-weight: 600; font-size: 22px;
    color: var(--ink);
    white-space: nowrap;
  }
  .contact-icon { width: 26px; height: 26px; flex: none; }

  .address {
    position: absolute;
    left: 600px; top: 464px;
    font-family: "Open Sans", sans-serif;
    font-weight: 600; font-size: 22px;
    line-height: 44px;
    color: var(--ink);
    font-style: normal;
    text-transform: uppercase;
    white-space: nowrap;
  }
</style>
</head>
<body>
  <section class="business-card">
    <div class="lower-planks">
      <div class="plank-seam" style="top: 186px;"></div>
    </div>

    <div class="tool-mark tool-mark--header" role="img" aria-label="Hand plane illustration with decorative swirl"></div>
    <h1 class="brand-name">Harlow's True Grain Woodwork</h1>

    <div class="tagline-band">
      <p class="tagline">We make it easy to get exactly what you're looking for.</p>
    </div>
    <div class="tool-mark tool-mark--band" role="img" aria-label="Hand plane illustration with decorative swirl"></div>

    <h2 class="owner-name">OWEN HARLOW</h2>

    <ul class="contact-list">
      <li class="contact-item">
        <svg class="contact-icon" viewBox="0 0 26 26" aria-hidden="true">
          <rect width="26" height="26" rx="4" fill="#121212"/>
          <path d="M8 6 l3 0 l1.5 4 l-2 1.5 q1.5 3 4 4.5 l1.5 -2 l4 1.5 l0 3 q-1 1.5 -3 1.5 q-10 -1 -11 -11 q0 -2 2 -3z" fill="#c7c3bb"/>
        </svg>
        <span>905 718-2265</span>
      </li>
      <li class="contact-item">
        <svg class="contact-icon" viewBox="0 0 26 26" aria-hidden="true">
          <rect width="26" height="26" rx="4" fill="#121212"/>
          <rect x="5" y="8" width="16" height="11" fill="none" stroke="#c7c3bb" stroke-width="1.8"/>
          <path d="M5 8 l8 6 l8 -6" fill="none" stroke="#c7c3bb" stroke-width="1.8"/>
        </svg>
        <span>harlowstruegrain@mailpost.example</span>
      </li>
      <li class="contact-item">
        <svg class="contact-icon" viewBox="0 0 26 26" aria-hidden="true">
          <rect width="26" height="26" rx="4" fill="#121212"/>
        </svg>
        <span>@harlowstruegrainwoodwork</span>
      </li>
    </ul>

    <address class="address">
      412 Birchmont Rd.<br>
      Niagara-on-the-Lake Ont.
    </address>
  </section>
</body>
</html>
```